Design Large Inspirational Artwork with Long Quote

Design a large piece of art with a quote from Marcus Hallwell.

QUOTE
"The thing that's so interesting about being alive is that you're all in. No matter what you do, you're all in. This is gonna kill you, so I think you might as well play the most magnificent game you can while you're waiting. Because, do you have anything better to do? Why not pick the best thing possible that you could do? Because you're more powerful than you think, way more powerful than you think. I mean, God only knows what you are in the final analysis. You're blind to your own weaknesses, but you're also blind to your own strengths. How far could you take that if you stopped wasting time, and if you stopped lying, and if you oriented yourself to the highest possible good that you could conceive of and you committed to that? How much good could you do? Well, I would say: why don't you find out?"

SIZE
A high-resolution print size of 6' wide and 3' tall should provide ample space for both the quote and the accompanying artwork.

TYPOGRAPHY
Choose a bold, clean, and easily readable font for the quote. You could also experiment with different font sizes for certain words or phrases to emphasize their importance within the quote.

COLORS
Since the quote is thought-provoking and reflective, you might want to use a color palette that evokes a sense of introspection and depth. Consider using cool, calming colors like shades of blue, gray, or green. Alternatively, you can use a contrasting color scheme with a light background and dark text to make the quote stand out.

ARTWORK
Select / create / edit background artwork to complement the quote.
While a great design might be minimalistic and/or greyscale, I'd really like to see some full color options. This might be anything from photography or graphics inspired by the ideas in the text, to abstract colors or illustrations that feel like the sentiment expressed.
The art should capture your attention and encourage you to read the text. The art should be visually appealing, both at a distance and up close, regardless of whether the text is read.
Updates

Having trouble confirming the exact print size.

Still looking for printing solution and final size confirmation.

Target Market(s)

Personal, business, office

Industry/Entity Type

None

Font styles to use
Sans Serif
Script

Requirements
Must have
• Entire quote, legible text, modern design, attractive artwork, approx 6ft wide and 3ft tall
Nice to have
• Different font (sizes) for certain words or phrases to emphasize their importance within the quote.

```html
<!DOCTYPE html>
<html lang="en">
<head>
<meta charset="utf-8">
<title>Marcus Hallwell – All In</title>
<link rel="stylesheet" href="https://fonts.googleapis.com/css2?family=Inter+Tight:ital,wght@0,500;1,700;1,800&family=Dancing+Script:wght@500&display=swap">
<style>
  :root {
    --page: #ffffff;
    --ink: #f4f1ea;
    --attribution: #8c8a86;
    --quote-mark: #8a6a3e;
    --sky: #8ec3ec;
    --sky-light: #dcecf6;
    --tunnel-gold: #b5893f;
    --tunnel-brown: #5a4224;
    --night: #050505;
  }
  html, body {
    margin: 0;
    width: 1200px;
    height: 804px;
    overflow: hidden;
    background: var(--page);
  }
  .artwork {
    position: absolute;
    top: 102px;
    left: 0;
    width: 1200px;
    height: 600px;
    overflow: hidden;
    background: linear-gradient(90deg, #2a2419 0%, #141210 45%, var(--night) 100%);
    font-family: "Inter Tight", "Helvetica Neue", Arial, sans-serif;
    color: var(--ink);
  }
  .tunnel-photo {
    position: absolute;
    inset: 0 auto 0 0;
    width: 620px;
    background:
      radial-gradient(ellipse 128px 142px at 240px 157px, var(--sky-light) 0%, var(--sky) 70%, rgba(142,195,236,0) 100%),
      radial-gradient(ellipse 260px 330px at 235px 250px, var(--tunnel-gold) 0%, var(--tunnel-brown) 50%, rgba(20,18,16,0) 100%);
    -webkit-mask-image: linear-gradient(90deg, #000 60%, transparent 100%);
            mask-image: linear-gradient(90deg, #000 60%, transparent 100%);
  }
  .quote {
    position: absolute;
    left: 403px;
    top: 0;
    width: 749px;
    height: 600px;
    text-shadow: 0 2px 4px rgba(0,0,0,.7);
  }
  .line {
    position: absolute;
    left: -40px;
    right: -40px;
    text-align: center;
    font-size: 18px;
    font-weight: 500;
    letter-spacing: -0.035em;
    white-space: nowrap;
    transform: translateY(-60%);
    line-height: 1;
  }
  .emph {
    font-style: italic;
    font-weight: 700;
    font-size: 34px;
    letter-spacing: -0.04em;
  }
  .emph--xl { font-size: 37px; font-weight: 800; }
  .emph--md { font-size: 29px; }
  .mark {
    position: absolute;
    width: 32px;
    height: 36px;
  }
  .mark--open { left: -30px; top: 72px; }
  .mark--close { left: 652px; top: 480px; }
  .attribution {
    position: absolute;
    left: 0;
    width: 749px;
    top: 518px;
    text-align: center;
    font-family: "Dancing Script", cursive;
    font-size: 22px;
    color: var(--attribution);
    text-shadow: none;
  }
</style>
</head>
<body>
  <section class="artwork">
    <div class="tunnel-photo" role="img" aria-label="Photo looking up a golden tunnel toward a circle of blue sky with clouds and a butterfly flying out"></div>

    <blockquote class="quote">
      <svg class="mark mark--open" viewBox="0 0 32 36" aria-hidden="true">
        <polygon points="4,0 14,0 10,36 0,36" fill="var(--quote-mark)"/>
        <polygon points="21,0 32,0 27,36 16,36" fill="var(--quote-mark)"/>
      </svg>

      <div class="line" style="top:104px">The thing that's so interesting about being alive is that you're <span class="emph">all in.</span> No matter what you do,</div>
      <div class="line" style="top:138px">you're all in. This is gonna kill you, so I think you might as well play the most magnificent game you</div>
      <div class="line" style="top:171px">can while you're waiting. Because, do you have anything better to do?</div>
      <div class="line" style="top:214px">Why not pick the <span class="emph">best thing possible</span> that you could do?</div>
      <div class="line" style="top:244px">Because you're more powerful than you think, way</div>
      <div class="line" style="top:281px"><span class="emph emph--xl">more powerful than you think.</span></div>
      <div class="line" style="top:319px">I mean, God only knows what you are in the final analysis.</div>
      <div class="line" style="top:352px">You're <span class="emph emph--md">blind to your own weaknesses,</span> but you're also</div>
      <div class="line" style="top:391px"><span class="emph emph--md">blind to your own strengths.</span> How far could you take that if you stopped wasting</div>
      <div class="line" style="top:425px">time, and if you stopped lying, and if you oriented yourself to the</div>
      <div class="line" style="top:458px"><span class="emph emph--md">highest possible good</span> that you could conceive of and you committed to that? How</div>
      <div class="line" style="top:491px">much good could you do? Well, I would say:&nbsp; why don't you find out?</div>

      <svg class="mark mark--close" viewBox="0 0 32 36" aria-hidden="true">
        <polygon points="0,0 11,0 7,36 2,36" fill="var(--quote-mark)"/>
        <polygon points="18,0 32,0 26,36 20,36" fill="var(--quote-mark)"/>
      </svg>

      <footer class="attribution">- Marcus Hallwell -</footer>
    </blockquote>
  </section>
</body>
</html>
```